Label Design for honey from a small farm in Italy

We need a label for our Acacia's honey .
We are a little farm in Italy and we would like something like organic, raw and simple.
Maybe with botanical drawing with different color like watercolor o something like that (very important natural and easy)
the jar for 1kg of honey: Capacity: 780 ml - Height: 137 mm - Diameter: ∅ 94 mm
- size approx h 5,5 x 10/14cm ( we use the same label for kg and 500 gr jar)

Industry/Entity Type

Farm

Requirements
Must have
• the writings:
- Acacia
- Miele italiano di Acacia
- Da consumarsi preferibilmente entro: ( and below the space to put the date by the hands)
- some space to put some presentation of the farm or some phrases
- our logo
- the space to put the weight by the hands
- Prodotto da Azienda Agricola ...(produced by Farm Name and address....)
- Confezionato presso Apicoltura... (packaged at apiculture Name and address..)
- graphic of Acacia’s flowers ( like drawing)
Should not have
• Barcode
nutritional table

```html
<!DOCTYPE html>
<html lang="it">
<head>
<meta charset="utf-8">
<title>Podere Lucina – Miele di Acacia</title>
<link rel="stylesheet" href="https://fonts.googleapis.com/css2?family=Antonio:wght@300;400;700&family=Lato:wght@400&family=Questrial&display=swap">
<style>
  :root {
    --backdrop: #3a3a3c;
    --paper: #ffffff;
    --mint: #b8e3d3;
    --mint-soft: #cdeee2;
    --mint-heading: #a3dcc8;
    --ink: #333333;
  }
  * { margin: 0; padding: 0; box-sizing: border-box; }
  html, body { width: 1200px; height: 543px; overflow: hidden; background: var(--backdrop); }
  .label {
    position: absolute; left: 84px; top: 84px; width: 1033px; height: 375px;
    background: var(--paper); overflow: hidden;
  }
  .section-heading {
    position: absolute; top: 52px; width: 260px; text-align: center;
    font-family: "Questrial", sans-serif; font-weight: 400; font-size: 17px; letter-spacing: 0.3px;
    color: var(--mint-heading); line-height: 1;
  }
  .copy {
    position: absolute; width: 270px; text-align: center;
    font-family: "Lato", sans-serif; font-weight: 400; font-size: 8.6px; line-height: 11.2px; color: var(--ink);
  }
  .heading-left { left: 38px; }
  .heading-right { left: 727px; }
  .copy-left-a { left: 38px; top: 85px; }
  .copy-left-b { left: 38px; top: 205px; }
  .copy-right { left: 727px; top: 85px; }
  .weight-box {
    position: absolute; left: 46px; top: 282px; width: 151px; height: 58px;
    background: var(--mint-soft); opacity: 0.8;
  }
  .note-panel {
    position: absolute; left: 723px; top: 207px; width: 276px; height: 122px;
    background: var(--mint); border-radius: 22px;
  }
  .note-panel .copy { position: static; width: 100%; padding-top: 12px; }
  .farm-scene {
    position: absolute; left: 230px; top: 176px; width: 305px; height: 199px;
    background: radial-gradient(closest-side at 50% 70%, rgba(184,227,211,0.45), rgba(184,227,211,0.18) 60%, rgba(255,255,255,0) 100%);
  }
  .brand-dot {
    position: absolute; left: 511px; top: 39px; width: 8px; height: 8px;
    border-radius: 50%; background: var(--mint);
  }
  .brand-name {
    position: absolute; left: 440px; top: 68px; width: 150px; text-align: center;
    font-family: "Antonio", sans-serif; font-weight: 700; font-size: 23px; letter-spacing: 0.5px;
    color: var(--mint); line-height: 1;
  }
  .title-block { position: absolute; left: 0; top: 0; width: 1033px; height: 375px; }
</style>
</head>
<body>
  <main class="label">
    <div class="farm-scene" role="img" aria-label="Disegno a linee di una cascina con silo, alberi, colline, nuvole e sole nascente"></div>

    <h2 class="section-heading heading-left">LOREM IPSUM DOLOR</h2>
    <p class="copy copy-left-a">Lorem ipsum dolor sit amet, consectetuer adipiscing elit, sed<br>diam nonummy nibh euismod tincidunt ut laoreet dolore magna<br>aliquam erat volutpat. Ut wisi enim ad minim veniam, quis<br>nostrud exerci tation ullamcorper suscipit lobortis nisl ut aliquip<br>ex ea commodo consequat. Duis autem vel eum iriure dolor in<br>hendrerit in vulputate velit esse molestie consequat, vel illum<br>dolore eu feugiat nulla facilisis at vero eros et accumsan et iusto<br>odio dignissim qui blandit praesent luptatum zzril delenit augue<br>duis dolore te feugait nulla facilisi.</p>
    <p class="copy copy-left-b">Lorem ipsum dolor sit amet, consectetuer adipiscing elit, sed<br>diam nonummy nibh euismod tincidunt ut laoreet dolore magna<br>aliquam erat volutpat.</p>
    <div class="weight-box"></div>

    <span class="brand-dot"></span>
    <div class="brand-name">PODERE LUCINA</div>

    <svg class="title-block" viewBox="0 0 1033 375" xmlns="http://www.w3.org/2000/svg">
      <g fill="#b8e3d3" font-family="Antonio, sans-serif">
        <text class="product-name" x="388" y="197" font-size="98" font-weight="700" textLength="263" lengthAdjust="spacingAndGlyphs">ACACIA</text>
        <rect class="rule" x="448" y="222" width="207" height="4"/>
        <text class="product-line" x="655" y="257" text-anchor="end" font-size="28" font-weight="400" textLength="134" lengthAdjust="spacingAndGlyphs">MIELE ITALIANO</text>
        <text class="product-line" x="655" y="284" text-anchor="end" font-size="28" font-weight="400" textLength="89" lengthAdjust="spacingAndGlyphs">DI ACACIA</text>
        <rect class="rule" x="524" y="292" width="131" height="4"/>
        <text class="net-weight" x="655" y="316" text-anchor="end" font-size="15" font-weight="300" textLength="81" lengthAdjust="spacingAndGlyphs">NET WT: 17.6 OZ</text>
        <text class="net-weight" x="655" y="333" text-anchor="end" font-size="15" font-weight="300" textLength="34" lengthAdjust="spacingAndGlyphs">[500G]</text>
      </g>
    </svg>

    <h2 class="section-heading heading-right">LOREM IPSUM DOLOR</h2>
    <p class="copy copy-right">Lorem ipsum dolor sit amet, consectetuer adipiscing elit, sed<br>diam nonummy nibh euismod tincidunt ut laoreet dolore magna<br>aliquam erat volutpat. Ut wisi enim ad minim veniam, quis<br>nostrud exerci tation ullamcorper suscipit lobortis nisl ut aliquip<br>ex ea commodo consequat. Duis autem vel eum iriure dolor in<br>hendrerit in vulputate velit esse molestie consequat, vel illum<br>dolore eu feugiat nulla facilisis at vero eros et accumsan et iusto<br>odio dignissim qui blandit praesent luptatum zzril delenit augue<br>duis dolore te feugait nulla facilisi.</p>

    <div class="note-panel">
      <p class="copy">Lorem ipsum dolor sit amet, consectetuer adipiscing elit, sed<br>diam nonummy nibh euismod tincidunt ut laoreet dolore<br>magna aliquam erat volutpat. Ut wisi enim ad minim veniam,<br>quis nostrud exerci tation ullamcorper suscipit lobortis nisl ut<br>aliquip ex ea commodo consequat. Duis autem vel eum iriure<br>dolor in hendrerit in vulputate velit esse molestie consequat, vel<br>illum dolore eu feugiat nulla facilisis at vero eros et accumsan et<br>iusto odio dignissim qui blandit praesent luptatum zzril delenit<br>augue duis dolore te feugait nulla facilisi.</p>
    </div>
  </main>
</body>
</html>
```